Powerpoint design for spirits and cosmetics packaging company

We need a powerpoint template that will be used for company presentations, projects, award ceremonies etc... We are packaging in the wine and spirits sector as well as in the cosmetics sector. Our job is to package our customers' bottles in gift boxes, to carry out labeling, quality control, etc. We are based in Cognac.
We work for the big names in luxury: QDRT, Vellane Ostrow, Trelumo, Syvanne etc...
The template should be neat with at least 10 different slides.
Cover page, summary page, product description page (several), page including a schedule, price presentation page.

Target Market(s)

premium spirits and cosmetics

Industry/Entity Type

Spiritueux et cosmétique

Font styles to use
Sans Serif

Requirements
Must have
• My project must have the logo attached, the possibility to add / modify photos afterwards. Must have about ten different slides

```html
<!DOCTYPE html>
<html lang="en">
<head>
<meta charset="utf-8">
<title>Maison Arlenne — Presentation Template</title>
<link href="https://fonts.googleapis.com/css2?family=Roboto+Condensed:wght@400;700&display=swap" rel="stylesheet">
<style>
  :root {
    --stage: #465a5f;
    --stage-deep: #34484d;
    --paper: #ffffff;
    --rose: #e8285a;
    --rose-soft: rgba(232, 40, 90, 0.82);
    --amber: #f4a54c;
    --amber-light: #f8c98f;
    --ink: #1c1c1c;
    --rule: #8a8a8a;
    --font: "Roboto Condensed", "Arial Narrow", sans-serif;
  }
  * { box-sizing: border-box; margin: 0; padding: 0; }
  html, body { width: 1200px; height: 800px; overflow: hidden; }
  body {
    background: linear-gradient(180deg, var(--stage-deep) 0%, var(--stage) 100%);
    font-family: var(--font);
    position: relative;
  }
  .slide-frame { position: absolute; overflow: hidden; box-shadow: 0 10px 28px rgba(0,0,0,0.28); }
  .slide-frame--cover { left: 240px; top: 30px; width: 720px; height: 405px; }
  .slide-frame--about { left: 70px; top: 478px; width: 520px; height: 292.5px; }
  .slide-frame--vision { left: 610px; top: 478px; width: 520px; height: 292.5px; }

  .slide {
    position: absolute; left: 0; top: 0;
    width: 960px; height: 540px;
    background: var(--paper);
    transform-origin: 0 0;
  }
  .slide-frame--cover .slide { transform: scale(0.75); }
  .slide-frame--about .slide,
  .slide-frame--vision .slide { transform: scale(0.541667); }

  .block { position: absolute; }
  .photo { position: absolute; }

  /* brand name, set as plain text */
  .brand { position: absolute; color: var(--rose); font-weight: 700; font-size: 15px; letter-spacing: 1.5px; line-height: 1.15; }
  .brand--small { font-size: 9px; letter-spacing: 1px; }

  /* cover */
  .cover__photo { left: 330px; top: 90px; width: 590px; height: 320px;
    background: linear-gradient(120deg, #6b4a3a 0%, #3d2b24 40%, #8a6b55 65%, #2a2a2c 100%); }
  .cover__accent { left: 750px; top: 35px; width: 170px; height: 170px; background: var(--rose-soft); }
  .cover__band { left: 55px; top: 150px; width: 400px; height: 225px; background: var(--rose-soft);
    display: flex; flex-direction: column; justify-content: center; padding-left: 30px; color: var(--paper); }
  .cover__title { font-size: 58px; font-weight: 400; line-height: 1; letter-spacing: 0.5px; }
  .cover__subtitle { font-size: 44px; font-weight: 400; line-height: 1.15; margin-top: 8px; }
  .cover__rule-v { left: 55px; top: 375px; width: 2px; height: 92px; background: var(--amber-light); }
  .cover__rule-h { left: 55px; top: 466px; width: 865px; height: 2px; background: var(--amber-light); }
  .cover__bar { left: 80px; top: 458px; width: 200px; height: 18px; background: var(--amber); }

  /* content slides */
  .section-title { position: absolute; left: 44px; top: 38px; color: var(--rose);
    font-size: 26px; font-weight: 400; padding-left: 12px; border-left: 2px solid var(--rose); }
  .section-title::after { content: ""; display: block; width: 80px; height: 6px; background: var(--rose); margin-top: 6px; }
  .body-copy { position: absolute; color: var(--ink); font-size: 15.5px; line-height: 1.42; }
  .body-copy p + p { margin-top: 20px; }
  .page-number { position: absolute; right: 28px; bottom: 26px; width: 26px; height: 26px;
    background: var(--rose); color: var(--paper); font-size: 12px; display: flex; align-items: center; justify-content: center; }
  .footer-rule { position: absolute; left: 120px; right: 60px; bottom: 38px; height: 1px; background: var(--rule); }

  .about__copy { left: 44px; top: 105px; width: 380px; }
  .about__photo { left: 560px; top: 70px; width: 340px; height: 400px;
    background: linear-gradient(150deg, #c9b6a8 0%, #b04a2e 45%, #7a1f1a 75%, #d4b08a 100%); }
  .about__accent-top { left: 760px; top: 45px; width: 160px; height: 170px; background: var(--rose-soft); }
  .about__accent-bottom { left: 540px; top: 340px; width: 110px; height: 130px; background: var(--rose-soft); }

  .vision__copy { left: 44px; top: 110px; width: 870px; font-size: 14px; }
  .vision__gallery { position: absolute; left: 60px; top: 245px; width: 840px; height: 210px; display: flex; gap: 14px; }
  .vision__gallery .photo { position: relative; flex: 1; height: 100%; }
  .vision__photo--a { background: linear-gradient(135deg, #8fa3b5, #d9dde2 60%, #6b7d8e); }
  .vision__photo--b { background: linear-gradient(135deg, #a7b3bd, #e3e6e8 55%, #7e8a93); }
  .vision__photo--c { background: linear-gradient(135deg, #3f6fb0, #c9d3de 55%, #e07a2e); }
  .vision__accent-left { left: 42px; top: 225px; width: 32px; height: 52px; background: var(--rose); }
  .vision__accent-right { left: 880px; top: 420px; width: 30px; height: 40px; background: var(--rose); }
</style>
</head>
<body>

<section class="slide-frame slide-frame--cover" aria-label="Cover slide">
  <div class="slide">
    <div class="brand" style="left:48px; top:42px;">MAISON<br>ARLENNE</div>
    <div class="photo cover__photo" role="img" aria-label="Photo of a spirits bottle on a packaging line"></div>
    <div class="block cover__accent"></div>
    <div class="block cover__band">
      <h1 class="cover__title">LOREM IPSUM</h1>
      <p class="cover__subtitle">LOREM IPSUM</p>
    </div>
    <div class="block cover__rule-v"></div>
    <div class="block cover__rule-h"></div>
    <div class="block cover__bar"></div>
  </div>
</section>

<section class="slide-frame slide-frame--about" aria-label="About us slide">
  <div class="slide">
    <h2 class="section-title">ABOUT US</h2>
    <div class="body-copy about__copy">
      <p>Lorem ipsum dolor sit amet, consectetuer adipiscing elit, sed diam nonummy nibh euismod tincidunt ut laoreet dolore magna aliquam erat volutpat. Ut wisi enim ad minim veniam, quis nostrud exerci tation ullamcorper suscipit lobortis nisl ut aliquip ex ea commodo consequat. Duis autem vel eum iriure dolor in hendrerit in vulputate velit esse molestie consequat, vel illum dolore eu feugiat nulla facilisis at vero eros et accumsan et iusto odio dignissim qui blandit praesent luptatum zzril delenit augue duis dolore te feugait nulla facilisi.</p>
      <p>Lorem ipsum dolor sit amet, cons ectetuer adip qui blandit praesent luptatum zzril delenit augue duis dolore te feugait nulla facilisi.</p>
    </div>
    <div class="photo about__photo" role="img" aria-label="Photo of hands fitting a cap on a perfume bottle"></div>
    <div class="block about__accent-top"></div>
    <div class="block about__accent-bottom"></div>
    <div class="brand brand--small" style="left:40px; bottom:28px;">MAISON<br>ARLENNE</div>
    <div class="page-number">02</div>
  </div>
</section>

<section class="slide-frame slide-frame--vision" aria-label="Our vision slide">
  <div class="slide">
    <h2 class="section-title">OUR VISION</h2>
    <div class="body-copy vision__copy">
      <p>Lorem ipsum dolor sit amet, consectetuer adipiscing elit, sed diam nonummy nibh euismod tincidunt ut laoreet dolore magna aliquam erat volutpat. Ut wisi enim ad minim veniam, quis nostrud exerci tation ullamcorper suscipit lobortis nisl ut aliquip ex ea commodo consequat. Duis autem vel eum iriure dolor in hendrerit in vulputate velit esse molestie consequat, vel illum dolore eu feugiat nulla facilisis at vero eros et accumsan et iusto odio dignissim qui blandit praesent luptatum zzril delenit augue duis dolore te feugait nulla facilisi.</p>
    </div>
    <div class="block vision__accent-left"></div>
    <div class="vision__gallery">
      <div class="photo vision__photo--a" role="img" aria-label="Photo of staff working at a packaging workshop"></div>
      <div class="photo vision__photo--b" role="img" aria-label="Photo of a wide production hall with packing tables"></div>
      <div class="photo vision__photo--c" role="img" aria-label="Photo of a labeling machine with blue boxes"></div>
    </div>
    <div class="block vision__accent-right"></div>
    <div class="brand brand--small" style="left:40px; bottom:28px;">MAISON<br>ARLENNE</div>
    <div class="footer-rule"></div>
    <div class="page-number">02</div>
  </div>
</section>

</body>
</html>
```